Keystone Lending and Capital. We provide MOSTLY residential home mortgages in Florida AND commercial loans for investment properties throughout the United states.
I would love to emulate so of the lender sites that are available on the internet but I would like to have the site as popular as possible for SEO purposes. Clients can already click the link to take them to the mortgage application where they can complete that and upload documents. If you could polish that up for me that would be great. I can also provide you with great detail on loan programs that are currently being offered. WE OFFER ALL MORTGAGE LENDING PRODUCTS. I would also like to add something in reference to the rate but I don't think it's legal to actually state or promise a rate for mortgage since they vary based on loan type, client and other criteria...

On the Keystone real estate site I would like to add a link or some way for clients to be able to put in credit card information to render services ...

Please let me know what you need from me

Thank you !!

Current link to site to improve and code

https://keystonelendingandcapital.example/

Residential and commmercial lending

Requirements
Must have
• Love to integrate Mortgage interest rates even if general
Nice to have
• Link to fill out mortgage application via Vanta LOS software

```html
<!DOCTYPE html>
<html lang="en">
<head>
<meta charset="utf-8">
<title>Keystone Lending and Capital — Residential &amp; Commercial Mortgage Lending</title>
<link rel="stylesheet" href="https://fonts.googleapis.com/css2?family=Lexend:wght@400;500;600;700;800&family=Inter:wght@400;500;600&family=Roboto+Slab:wght@600&display=swap">
<style>
:root{
  --green-dark:#1f3d24;
  --green-deep:#27462b;
  --green:#7db63a;
  --green-soft:#eef7e6;
  --ink:#1b1d1c;
  --body:#6a6d6b;
  --line:#e3e6e4;
  --white:#ffffff;
}
*{box-sizing:border-box;margin:0;padding:0}
html,body{width:1200px;height:4227px;overflow:hidden}
body{position:relative;font-family:"Inter",sans-serif;color:var(--body);background:var(--white);font-size:12px;line-height:19px}
h1,h2,h3,h4{font-family:"Lexend",sans-serif;color:var(--ink);font-weight:500}
.abs{position:absolute}
.eyebrow{font-family:"Roboto Slab",serif;font-weight:600;font-size:12px;color:var(--ink)}
.btn{position:absolute;display:flex;align-items:center;justify-content:center;font-family:"Lexend",sans-serif;font-size:11px;font-weight:500;color:var(--white);background:var(--green);text-decoration:none}

/* top bar */
.topbar{top:0;left:0;width:1200px;height:33px;background:var(--green-dark);color:var(--white);font-size:10px;line-height:33px}
.topbar .social{position:absolute;left:110px;top:12px;display:flex;gap:19px}
.topbar .social span{width:8px;height:8px;border-radius:50%;background:var(--white)}
.topbar .links{position:absolute;left:267px;display:flex;gap:18px}
.topbar .links span::before{content:"•";color:var(--green);margin-right:5px}
.topbar .contact{position:absolute;left:700px;display:flex;gap:22px}
.topbar .contact span{display:flex;align-items:center;gap:6px}
.topbar svg{width:10px;height:10px;stroke:var(--white);fill:none;stroke-width:1.6}

/* header */
.header{top:33px;left:0;width:1200px;height:85px;background:var(--white)}
.brand{position:absolute;left:102px;top:14px;display:flex;align-items:center;gap:8px}
.brand-mark{width:44px;height:44px;background:var(--green-dark)}
.brand-name{font-family:"Lexend",sans-serif;font-weight:500;font-size:8px;line-height:11px;color:var(--green);letter-spacing:.4px;text-transform:uppercase}
.nav{position:absolute;left:470px;top:34px}
.nav a{font-family:"Lexend",sans-serif;font-size:12px;font-weight:500;color:var(--ink);text-decoration:none;position:absolute;white-space:nowrap}
.header .btn{left:988px;top:28px;width:112px;height:28px}

/* hero */
.hero{top:118px;left:0;width:1200px;height:596px;background:linear-gradient(90deg,rgba(24,24,20,.82) 0%,rgba(40,34,28,.55) 45%,rgba(120,100,80,.25) 100%),linear-gradient(135deg,#3d3a33 0%,#6b5a48 45%,#a48c70 75%,#c9b7a0 100%)}
.hero h1{position:absolute;left:100px;top:214px;width:520px;font-size:31px;line-height:37px;font-weight:800;color:var(--white);text-transform:uppercase;letter-spacing:-1.2px}
.hero p{position:absolute;left:100px;top:339px;font-size:10px;color:var(--white);font-weight:500;text-transform:uppercase}
.hero .btn-quote{left:100px;top:371px;width:146px;height:36px;border:2px solid #a6d46b}
.hero .btn-app{left:263px;top:371px;width:192px;height:36px;background:transparent;border:2px solid var(--white)}

/* about */
.about{top:714px;left:0;width:1200px;height:560px}
.soft-panel{position:absolute;left:600px;top:50px;width:540px;height:480px;background:linear-gradient(180deg,#f7f8f7,#ffffff)}
.dash-v{position:absolute;left:118px;top:170px;height:300px;border-left:1px dashed #bfc5c1}
.dash-h{position:absolute;left:118px;top:470px;width:40px;border-top:1px dashed #bfc5c1}
.photo-main{position:absolute;left:131px;top:87px;width:457px;height:315px;background:linear-gradient(160deg,#d9d4cc 0%,#b79d83 45%,#6f7f8a 80%,#8a8278 100%)}
.photo-small{position:absolute;left:80px;top:70px;width:190px;height:120px;background:var(--white);padding:6px;box-shadow:0 4px 16px rgba(0,0,0,.12)}
.photo-small div{width:100%;height:100%;background:linear-gradient(135deg,#5b5e63,#c9c5bf 60%,#8d8e8f)}
.exp-card{position:absolute;left:156px;top:402px;width:469px;height:100px;background:var(--white);box-shadow:0 8px 26px rgba(0,0,0,.09)}
.exp-card .num{position:absolute;left:40px;top:22px;font-family:"Lexend",sans-serif;font-weight:700;font-size:34px;color:var(--ink);line-height:36px}
.exp-card .lbl{position:absolute;left:24px;top:62px;font-size:11px;color:var(--ink)}
.exp-card .sep{position:absolute;left:156px;top:22px;height:48px;border-left:2px solid var(--ink)}
.exp-card p{position:absolute;left:171px;top:20px;width:270px;font-size:11px;line-height:18px}
.about-copy{position:absolute;left:650px;top:130px;width:470px}
.about-copy h2{margin-top:14px;width:370px;font-size:29px;line-height:33px;letter-spacing:-.3px}
.about-copy p{margin-top:16px;font-size:11.5px;line-height:19px}
.about-copy p+p{margin-top:10px}
.about .btn{left:650px;top:418px;width:120px;height:28px}

/* features */
.features{top:1297px;left:100px;width:1000px;height:165px;display:flex}
.feature{flex:1;text-align:center;padding-top:28px;position:relative}
.feature+.feature{border-left:1px solid var(--line)}
.feature svg{width:30px;height:30px;stroke:var(--green);fill:none;stroke-width:1.4}
.feature h3{margin-top:8px;font-size:17px}
.feature p{margin:6px auto 0;width:290px;font-size:11.5px;line-height:19px}

/* offer */
.offer{top:1548px;left:0;width:1200px;height:434px;background:linear-gradient(90deg,rgba(31,61,36,.94) 0%,rgba(38,70,42,.86) 40%,rgba(56,88,56,.78) 100%),linear-gradient(135deg,#3f5a3e,#7a8a6a 50%,#445c44)}
.offer .eyebrow{position:absolute;left:100px;top:86px;color:#a8d46e}
.offer h2{position:absolute;left:100px;top:116px;width:340px;font-size:29px;line-height:33px;color:var(--white)}
.offer p.lead{position:absolute;left:100px;top:236px;width:330px;font-size:11.5px;line-height:19px;color:var(--white)}
.offer .btn{left:100px;top:315px;width:116px;height:28px}
.offer-cards{position:absolute;left:483px;top:89px;display:grid;grid-template-columns:repeat(3,195px);gap:16px}
.offer-card{height:254px;background:rgba(255,255,255,.14);padding:22px 24px}
.offer-card .ico{width:34px;height:34px;border-radius:50%;background:var(--green);display:flex;align-items:center;justify-content:center}
.offer-card .ico svg{width:14px;height:14px;stroke:var(--white);fill:none;stroke-width:1.8}
.offer-card h4{margin-top:16px;font-size:13px;line-height:16px;color:var(--white);font-weight:600}
.offer-card p{margin-top:8px;font-size:11.5px;line-height:19px;color:#dfe7dc}

/* listing */
.listing{top:1982px;left:0;width:1200px;height:727px}
.listing .eyebrow{position:absolute;left:100px;top:74px}
.listing h2{position:absolute;left:100px;top:104px;width:320px;font-size:29px;line-height:33px;font-weight:600}
.listing p.lead{position:absolute;left:509px;top:124px;width:590px;font-size:11.5px;line-height:19px}
.listing .rule{position:absolute;left:509px;top:200px;width:56px;border-top:2px solid var(--green)}
.props{position:absolute;left:100px;top:244px;display:grid;grid-template-columns:repeat(4,238px);gap:16px}
.prop{height:422px;background:var(--white);box-shadow:0 6px 22px rgba(0,0,0,.08);position:relative}
.prop .img{height:174px;position:relative}
.prop:nth-child(1) .img{background:linear-gradient(180deg,#6f87ad 0%,#9aa8bb 40%,#8a7a6a 75%,#5b5a4e)}
.prop:nth-child(2) .img{background:linear-gradient(180deg,#606266 0%,#45474a 55%,#3a3b3d)}
.prop:nth-child(3) .img{background:linear-gradient(180deg,#2e3c6a 0%,#4b5b88 45%,#8d7a5e 80%,#3f4a38)}
.prop:nth-child(4) .img{background:linear-gradient(180deg,#27396a 0%,#6d6a6a 50%,#8a6a4a 85%,#3b3a32)}
.prop .img::after{content:"";position:absolute;inset:0;background:linear-gradient(180deg,transparent 50%,rgba(0,0,0,.45))}
.prop .type{position:absolute;left:20px;top:114px;z-index:1;font-family:"Roboto Slab",serif;font-size:11px;color:#d6a94a}
.prop .price{position:absolute;left:20px;top:134px;z-index:1;font-family:"Lexend",sans-serif;font-weight:700;font-size:16px;color:var(--white)}
.prop h3{position:absolute;left:20px;top:194px;font-size:16px;font-weight:600}
.prop .addr{position:absolute;left:20px;top:216px;font-size:9.5px}
.prop .desc{position:absolute;left:20px;top:248px;width:200px;font-size:11px;line-height:19px}
.prop .meta{position:absolute;left:20px;top:326px;display:flex;gap:12px;font-size:9px;color:var(--ink)}
.prop .meta span,.prop .sqft{display:flex;align-items:center;gap:5px}
.prop .sqft{position:absolute;left:20px;top:344px;font-size:9px;color:var(--ink)}
.prop svg{width:10px;height:10px;fill:var(--ink)}
.prop .btn{left:20px;top:376px;width:198px;height:30px}

/* testimonials */
.testimonials{top:2709px;left:0;width:1200px;height:596px}
.map{position:absolute;left:220px;top:60px;width:760px;height:470px;background:radial-gradient(ellipse at 50% 45%,rgba(214,220,226,.55),rgba(255,255,255,0) 70%)}
.testimonials .head{position:absolute;left:0;top:108px;width:1200px;text-align:center}
.testimonials h2{margin-top:8px;font-size:29px;line-height:36px}
.testimonials .head p{margin:8px auto 0;width:600px;font-size:11.5px;line-height:19px}
.quotes{position:absolute;left:100px;top:256px;display:grid;grid-template-columns:repeat(3,320px);gap:20px}
.quote{position:relative;height:250px;background:var(--white);border:4px double #cfd7e1;padding:22px 24px}
.stars{color:var(--green);font-size:14px;letter-spacing:6px}
.quote p{margin-top:16px;font-size:12px;line-height:21px}
.person{position:absolute;left:24px;top:176px;display:flex;align-items:center;gap:12px}
.avatar{width:40px;height:40px;border-radius:50%;background:linear-gradient(135deg,#c9ccd2,#8e949c);border:3px solid #eef0f2}
.person b{display:block;font-family:"Lexend",sans-serif;font-weight:500;font-size:11px;color:var(--ink);line-height:15px}
.person span{font-size:10px}

/* appointment */
.appointment{top:3305px;left:0;width:1200px;height:537px;background:linear-gradient(90deg,rgba(31,61,36,.96),rgba(33,64,38,.9)),linear-gradient(135deg,#3b5a3a,#6b7d5c)}
.vert{position:absolute;left:-165px;top:268px;transform:rotate(-90deg);font-family:"Lexend",sans-serif;font-weight:700;font-size:68px;line-height:76px;color:rgba(255,255,255,.1);width:450px;text-align:center}
.appointment .intro{position:absolute;left:112px;top:86px;width:460px;color:var(--white)}
.appointment h2{font-size:29px;line-height:33px;color:var(--white)}
.appointment .intro>p{margin-top:16px;font-size:11.5px;line-height:19px}
.point{margin-top:20px}
.point h4{margin-left:21px;font-size:13px;color:var(--white);font-weight:500}
.point p{margin-top:8px;font-size:11.5px;line-height:19px}
.form-card{position:absolute;left:629px;top:49px;width:471px;height:534px;background:var(--white);box-shadow:0 10px 30px rgba(0,0,0,.12);padding:34px 38px}
.form-card h2{font-size:27px;line-height:34px;color:var(--ink)}
.form-card>p{margin-top:6px;font-size:11.5px;line-height:19px;width:380px}
.fields{margin-top:22px;display:grid;grid-template-columns:186px 194px;column-gap:18px;row-gap:14px}
.field label{display:block;font-size:11px;color:var(--ink);font-weight:500}
.field .in{margin-top:6px;height:26px;border-bottom:1px solid var(--line);padding:0 14px 0 12px;font-size:11px;color:#a3a7a5;display:flex;align-items:center;justify-content:space-between}
.field .in svg{width:11px;height:11px;stroke:var(--ink);fill:none;stroke-width:1.6}
.field.full{grid-column:1/3}
.field.full .in{height:84px;align-items:flex-start;padding-top:2px}
.form-card .btn{left:38px;top:460px;width:395px;height:36px}

/* footer */
.footer{top:3842px;left:0;width:1200px;height:371px;background:var(--green-soft)}
.footer .brand{left:100px;top:118px}
.footer .about-text{position:absolute;left:100px;top:168px;width:240px;font-size:11.5px;line-height:19px}
.call{position:absolute;left:100px;top:263px;display:flex;align-items:center;gap:10px}
.call .circ{width:34px;height:34px;border-radius:50%;background:var(--green-dark);display:flex;align-items:center;justify-content:center}
.call svg{width:14px;height:14px;stroke:var(--white);fill:none;stroke-width:1.8}
.call small{display:block;font-size:10px;color:var(--ink);line-height:12px}
.call b{font-family:"Lexend",sans-serif;font-weight:600;font-size:17px;color:var(--ink)}
.fcol{position:absolute;top:126px}
.fcol h4{font-size:13px;font-weight:500}
.fcol ul{list-style:none;margin-top:8px}
.fcol li{height:28px;line-height:28px;font-size:11.5px;border-bottom:1px solid #dfe6da}
.fcol li:last-child{border-bottom:0}
.fcol.services{left:400px;width:171px}
.fcol.support{left:599px;width:174px}
.touch{position:absolute;left:801px;top:98px;width:299px;height:220px;background:var(--green-soft);border:4px double #c8d3de;padding:26px 28px}
.touch h4{font-size:13px;font-weight:500}
.touch .row{display:flex;gap:8px;margin-top:10px;font-size:11.5px;line-height:19px;color:var(--ink)}
.touch .row+.row{margin-top:4px}
.touch svg{flex:none;width:11px;height:11px;margin-top:4px;stroke:var(--ink);fill:none;stroke-width:1.6}
.touch .soc{display:flex;gap:8px;margin-top:14px}
.touch .soc span{width:26px;height:26px;border-radius:50%;border:1.5px solid var(--ink)}
.bottom{top:4213px;left:0;width:1200px;height:14px;background:var(--green);overflow:hidden;font-size:9px;line-height:20px;color:var(--white);padding-left:100px}
</style>
</head>
<body>

<div class="abs topbar">
  <div class="social"><span></span><span></span><span></span><span></span><span></span></div>
  <div class="links"><span>Support</span><span>Live Chat</span></div>
  <div class="contact">
    <span><svg viewBox="0 0 12 12"><path d="M2 1.5h2l1 2.5-1.3 1a6 6 0 0 0 3.3 3.3l1-1.3 2.5 1v2a1 1 0 0 1-1 1A9 9 0 0 1 1 2.5a1 1 0 0 1 1-1z"/></svg>(+1) 305-555-0148</span>
    <span><svg viewBox="0 0 12 12"><rect x="1" y="2.5" width="10" height="7"/><path d="M1 2.5l5 4 5-4"/></svg>hello@keystonelending.example</span>
    <span><svg viewBox="0 0 12 12"><circle cx="6" cy="6" r="5"/><path d="M6 3v3l2 1.5"/></svg>Mon - Fri : 09.00-17.00</span>
  </div>
</div>

<header class="abs header">
  <div class="brand"><div class="brand-mark"></div><div class="brand-name">Keystone Lending and Capital<br>of Florida</div></div>
  <nav class="nav">
    <a href="#" style="left:17px">Home</a>
    <a href="#" style="left:91px">About</a>
    <a href="#" style="left:175px">Services</a>
    <a href="#" style="left:273px">Properties</a>
    <a href="#" style="left:367px">Contact</a>
  </nav>
  <a class="btn" href="#">APPLY NOW</a>
</header>

<section class="abs hero" role="img" aria-label="Photo of a smiling couple signing mortgage papers with a loan officer">
  <h1>Your best resource for hassle-free, low cost mortgage origination</h1>
  <p>Residential home loans in Florida and commercial lending in America</p>
  <a class="btn btn-quote" href="#">GET FREE QUOTE</a>
  <a class="btn btn-app" href="#">MORTGAGE APPLICATION</a>
</section>

<section class="abs about">
  <div class="soft-panel" role="img" aria-label="Faint decorative dot pattern background"></div>
  <div class="dash-v"></div><div class="dash-h"></div>
  <div class="photo-main" role="img" aria-label="Photo of a couple reviewing a tablet among moving boxes in their new home"></div>
  <div class="photo-small"><div role="img" aria-label="Photo of a loan officer handing over a small house model"></div></div>
  <div class="exp-card">
    <div class="num">20+</div>
    <div class="lbl">Years Experience</div>
    <div class="sep"></div>
    <p>Vitae lorem risus venenatis facilisis mattis curabitur porttitor platea. Volutpat fringilla sapien fusce lectus urna placerat.</p>
  </div>
  <div class="about-copy">
    <div class="eyebrow">Who We Are</div>
    <h2>Find the most suitable mortgage for your ideal property</h2>
    <p>Morbi eget maximus habitasse id malesuada mi hendrerit. Magnis volutpat mi consectetur etiam suspendisse pellentesque nostra odio. Ridiculus inceptos eleifend dolor porttitor orci natoque penatibus.</p>
    <p>Magna non dolor facilisis sodales proin. Lobortis sagittis imperdiet litora laoreet erat vivamus habitasse at malesuada.</p>
  </div>
  <a class="btn" href="#">More About Us</a>
</section>

<section class="abs features">
  <div class="feature">
    <svg viewBox="0 0 30 30"><rect x="6" y="5" width="18" height="22"/><path d="M15 5v22M9 10h3M9 15h3M9 20h3M18 10h3M18 15h3M18 20h3"/></svg>
    <h3>Home Purchase</h3>
    <p>Sagittis fames convallis aptent risus himenaeos feugiat taciti dictumst class cras.</p>
  </div>
  <div class="feature">
    <svg viewBox="0 0 30 30"><rect x="7" y="3" width="16" height="24" rx="1"/><rect x="10" y="6" width="10" height="5"/><path d="M10 15h2M14 15h2M18 15h2M10 19h2M14 19h2M18 19h2M10 23h2M14 23h2M18 23h2"/></svg>
    <h3>Refinance</h3>
    <p>Sagittis fames convallis aptent risus himenaeos feugiat taciti dictumst class cras.</p>
  </div>
  <div class="feature">
    <svg viewBox="0 0 30 30"><rect x="4" y="8" width="22" height="17" rx="2"/><path d="M7 8l12-4 2 4M18 14h8v6h-8z"/><circle cx="21" cy="17" r="1"/></svg>
    <h3>Loan Options</h3>
    <p>Sagittis fames convallis aptent risus himenaeos feugiat taciti dictumst class cras.</p>
  </div>
</section>

<section class="abs offer" role="img" aria-label="Green-tinted photo of a couple meeting with a mortgage advisor">
  <div class="eyebrow">What We Offer</div>
  <h2>Navigating Mortgages with Ease and Confidence</h2>
  <p class="lead">Vulputate pretium malesuada posuere suscipit vehicula venenatis eget ex. Mattis sapien ridiculus est nibh lectus suspendisse.</p>
  <a class="btn" href="#">Discover More</a>
  <div class="offer-cards">
    <div class="offer-card"><div class="ico"><svg viewBox="0 0 14 14"><path d="M3 11L11 3M5 3h6v6"/></svg></div><h4>Mortgage<br>Consultation</h4><p>Quisque amet sit nascetur fermentum eu erat curabitur aliquet iaculis lacus semper. Dis integer nibh dignissim per nec ut.</p></div>
    <div class="offer-card"><div class="ico"><svg viewBox="0 0 14 14"><path d="M3 11L11 3M5 3h6v6"/></svg></div><h4>Mortgage Refinancing</h4><p>Quisque amet sit nascetur fermentum eu erat curabitur aliquet iaculis lacus semper. Dis integer nibh dignissim per nec ut.</p></div>
    <div class="offer-card"><div class="ico"><svg viewBox="0 0 14 14"><path d="M3 11L11 3M5 3h6v6"/></svg></div><h4>Mortgage Insurance</h4><p>Quisque amet sit nascetur fermentum eu erat curabitur aliquet iaculis lacus semper. Dis integer nibh dignissim per nec ut.</p></div>
  </div>
</section>

<section class="abs listing">
  <div class="eyebrow">Listing Property</div>
  <h2>Empowering Your Homeownership Journey</h2>
  <p class="lead">Senectus tristique lacus litora placerat sollicitudin penatibus quis. Inceptos consequat habitasse praesent ipsum ante quisque integer pellentesque taciti fermentum. Luctus ex sapien consectetur venenatis mus.</p>
  <div class="rule"></div>
  <div class="props">
    <article class="prop">
      <div class="img" role="img" aria-label="Photo of a row of Victorian houses"></div>
      <div class="type">House</div><div class="price">$110,000-$199,000</div>
      <h3>Balaraja Garden City</h3><div class="addr">12 Sunset Street</div>
      <p class="desc">Primis aliquam praesent pulvinar metus mus magnis placerat vehicula enim.</p>
      <div class="meta"><span><svg viewBox="0 0 10 10"><path d="M0 3h1v2h9v4H9V7H1v2H0zM2 3h3v2H2z"/></svg>2 Beds</span><span><svg viewBox="0 0 10 10"><path d="M1 1h2v4h7v1a3 3 0 0 1-3 3H4a3 3 0 0 1-3-3z"/></svg>2 Bath</span><span><svg viewBox="0 0 10 10"><path d="M1 5l1-3h6l1 3v3H8V7H2v1H1z"/></svg>1 Parking lot</span></div>
      <div class="sqft"><svg viewBox="0 0 10 10"><path d="M1 1h2v6h6v2H1z"/></svg>1250sqft</div>
      <a class="btn" href="#">Apply Now</a>
    </article>
    <article class="prop">
      <div class="img" role="img" aria-label="Photo of a modern grey apartment block"></div>
      <div class="type">Apartment</div><div class="price">$50,000-$99,000</div>
      <h3>Ophelia Apartment</h3><div class="addr">34 Union Avenue</div>
      <p class="desc">Primis aliquam praesent pulvinar metus mus magnis placerat vehicula enim.</p>
      <div class="meta"><span><svg viewBox="0 0 10 10"><path d="M0 3h1v2h9v4H9V7H1v2H0zM2 3h3v2H2z"/></svg>2 Beds</span><span><svg viewBox="0 0 10 10"><path d="M1 1h2v4h7v1a3 3 0 0 1-3 3H4a3 3 0 0 1-3-3z"/></svg>2 Bath</span><span><svg viewBox="0 0 10 10"><path d="M1 5l1-3h6l1 3v3H8V7H2v1H1z"/></svg>1 Parking lot</span></div>
      <div class="sqft"><svg viewBox="0 0 10 10"><path d="M1 1h2v6h6v2H1z"/></svg>1250sqft</div>
      <a class="btn" href="#">Apply Now</a>
    </article>
    <article class="prop">
      <div class="img" role="img" aria-label="Photo of a lit suburban house at dusk"></div>
      <div class="type">Office &amp; Apartment</div><div class="price">$80,000-$150,000</div>
      <h3>Twin Tower Office</h3><div class="addr">56 Washington Street</div>
      <p class="desc">Primis aliquam praesent pulvinar metus mus magnis placerat vehicula enim.</p>
      <div class="meta"><span><svg viewBox="0 0 10 10"><path d="M0 3h1v2h9v4H9V7H1v2H0zM2 3h3v2H2z"/></svg>2 Beds</span><span><svg viewBox="0 0 10 10"><path d="M1 1h2v4h7v1a3 3 0 0 1-3 3H4a3 3 0 0 1-3-3z"/></svg>2 Bath</span><span><svg viewBox="0 0 10 10"><path d="M1 5l1-3h6l1 3v3H8V7H2v1H1z"/></svg>1 Parking lot</span></div>
      <div class="sqft"><svg viewBox="0 0 10 10"><path d="M1 1h2v6h6v2H1z"/></svg>1250sqft</div>
      <a class="btn" href="#">Apply Now</a>
    </article>
    <article class="prop">
      <div class="img" role="img" aria-label="Photo of a modern timber-clad house at dusk"></div>
      <div class="type">House</div><div class="price">$140,000-$220,000</div>
      <h3>Serpong Smart Town</h3><div class="addr">78 Oak Boulevard</div>
      <p class="desc">Primis aliquam praesent pulvinar metus mus magnis placerat vehicula enim.</p>
      <div class="meta"><span><svg viewBox="0 0 10 10"><path d="M0 3h1v2h9v4H9V7H1v2H0zM2 3h3v2H2z"/></svg>2 Beds</span><span><svg viewBox="0 0 10 10"><path d="M1 1h2v4h7v1a3 3 0 0 1-3 3H4a3 3 0 0 1-3-3z"/></svg>2 Bath</span><span><svg viewBox="0 0 10 10"><path d="M1 5l1-3h6l1 3v3H8V7H2v1H1z"/></svg>1 Parking lot</span></div>
      <div class="sqft"><svg viewBox="0 0 10 10"><path d="M1 1h2v6h6v2H1z"/></svg>1250sqft</div>
      <a class="btn" href="#">Apply Now</a>
    </article>
  </div>
</section>

<section class="abs testimonials">
  <div class="map" role="img" aria-label="Faint dotted world map background"></div>
  <div class="head">
    <div class="eyebrow">Testimonials</div>
    <h2>What our clients say about us</h2>
    <p>Lorem ipsum dolor sit amet, consectetur adipiscing elit. Ut elit tellus, luctus nec ullamcorper mattis, pulvinar dapibus leo.</p>
  </div>
  <div class="quotes">
    <div class="quote"><div class="stars">★★★★☆</div><p>Porttitor integer bibendum odio pulvinar rutrum magnis viverra orci tincidunt efficitur. Aptent pharetra est nunc mattis donec per mi porttitor.</p><div class="person"><div class="avatar" role="img" aria-label="Client portrait"></div><div><b>Marisa T. Lowell</b><span>Bandung</span></div></div></div>
    <div class="quote"><div class="stars">★★★★★</div><p>Porttitor integer bibendum odio pulvinar rutrum magnis viverra orci tincidunt efficitur. Aptent pharetra est nunc mattis donec per mi porttitor.</p><div class="person"><div class="avatar" role="img" aria-label="Client portrait"></div><div><b>Dennis R. Halvorsen</b><span>Semarang</span></div></div></div>
    <div class="quote"><div class="stars">★★★★★</div><p>Porttitor integer bibendum odio pulvinar rutrum magnis viverra orci tincidunt efficitur. Aptent pharetra est nunc mattis donec per mi porttitor.</p><div class="person"><div class="avatar" role="img" aria-label="Client portrait"></div><div><b>Owen P. Whitfield</b><span>Jakarta</span></div></div></div>
  </div>
</section>

<section class="abs appointment" role="img" aria-label="Green-tinted photo of a house model and keys on a desk">
  <div class="vert">Appointment</div>
  <div class="intro">
    <h2>Let's Talk with a Lending Specialist</h2>
    <p>Vulputate pretium malesuada posuere suscipit vehicula venenatis eget ex. Mattis sapien ridiculus est nibh lectus suspendisse.</p>
    <div class="point"><h4>Every Step Of The Way</h4><p>Pharetra tellus aliquet lacus fusce fermentum malesuada sem. Purus suscipit ullamcorper elementum in rhoncus montes.</p></div>
    <div class="point"><h4>Dedicated Loan Concierge</h4><p>Pharetra tellus aliquet lacus fusce fermentum malesuada sem. Purus suscipit ullamcorper elementum in rhoncus montes.</p></div>
    <div class="point"><h4>Flexible Rates &amp; Low Fees</h4><p>General rates today: 30-yr fixed from about 6.5%, 15-yr fixed from about 5.8%. Rates vary by loan type and credit; not a quote.</p></div>
  </div>
  <form class="form-card">
    <h2>Make an Appointment</h2>
    <p>Senectus himenaeos lectus nunc aptent morbi dis. Tempus bibendum mollis egestas tempor justo magna.</p>
    <div class="fields">
      <div class="field"><label>First Name</label><div class="in">First Name</div></div>
      <div class="field"><label>Last Name</label><div class="in">Last Name</div></div>
      <div class="field"><label>Phone</label><div class="in">Phone</div></div>
      <div class="field"><label>Email</label><div class="in">Email</div></div>
      <div class="field"><label>Date</label><div class="in" style="color:var(--ink)">mm/dd/yyyy<svg viewBox="0 0 11 11"><rect x="1" y="2" width="9" height="8"/><path d="M1 4.5h9"/></svg></div></div>
      <div class="field"><label>Time</label><div class="in" style="color:var(--ink)">--:-- --<svg viewBox="0 0 11 11"><circle cx="5.5" cy="5.5" r="4.5"/><path d="M5.5 3v2.5l1.7 1"/></svg></div></div>
      <div class="field full"><label>Message</label><div class="in">Message</div></div>
    </div>
    <a class="btn" href="#">Make Appointment</a>
  </form>
</section>

<footer class="abs footer">
  <div class="brand"><div class="brand-mark"></div><div class="brand-name">Keystone Lending and Capital<br>of Florida</div></div>
  <p class="about-text">Nunc senectus justo id ad ultrices dignissim. Volutpat ullamcorper ut arcu tellus metus porttitor phasellus purus.</p>
  <div class="call"><div class="circ"><svg viewBox="0 0 14 14"><path d="M2.5 1.5h2.3l1.2 3-1.5 1.1a7 7 0 0 0 3.9 3.9l1.1-1.5 3 1.2v2.3a1 1 0 0 1-1 1A11 11 0 0 1 1.5 2.5a1 1 0 0 1 1-1z"/></svg></div><div><small>Call Anytime</small><b>888 555-0192</b></div></div>
  <div class="fcol services"><h4>Services</h4><ul><li>Bridge Loan</li><li>Rental Loan</li><li>Overseas Mortgage</li><li>Mortgage Refinancing</li><li>Consultation</li></ul></div>
  <div class="fcol support"><h4>Support</h4><ul><li>Help Center</li><li>Customer Service</li><li>Sales Support</li><li>FAQ</li><li>Contact Us</li></ul></div>
  <div class="touch">
    <h4>Get in Touch</h4>
    <div class="row"><svg viewBox="0 0 11 11"><path d="M5.5 10S2 6.5 2 4.3a3.5 3.5 0 0 1 7 0C9 6.5 5.5 10 5.5 10z"/><circle cx="5.5" cy="4.3" r="1.2"/></svg>1420 Harbor Palm Way, Tampa - Florida</div>
    <div class="row"><svg viewBox="0 0 11 11"><rect x="1" y="2.5" width="9" height="6.5"/><path d="M1 2.5l4.5 3.5 4.5-3.5"/></svg>hello@keystonelending.example</div>
    <div class="row"><svg viewBox="0 0 11 11"><path d="M2 1.5h2l1 2.3-1.2 1a5.5 5.5 0 0 0 2.9 2.9l1-1.2 2.3 1v2a1 1 0 0 1-1 1A8 8 0 0 1 1 2.5a1 1 0 0 1 1-1z"/></svg>+1 305.555.0148</div>
    <div class="soc"><span></span><span></span><span></span><span></span><span></span></div>
  </div>
</footer>
<div class="abs bottom">Copyright © 2025 Keystone Lending and Capital. All rights reserved.</div>

</body>
</html>
```